Banner Design 4040mm W x 2190mm H

Design a glamorous and exciting 4040mm W x 2190mm H backdrop for the QRLMT Velvet Orchid Gala at the luxurious Tallow Hall, Fenwick, Mirrabelle, Sydney. This exciting backdrop should be spectacular so that people will be excited to take photos in front of it.
Design Colours preferred is black and pink.
Please include our website on the banner www.qrlmt.org.au
Should include the words "QRLMT Velvet Orchid Gala" as the main attraction on the banner.
Please include "Thank you to our sponsors" and include the logo of the sponsors.
Sponsors:
Brockden Pathology
EastGlen Radiology
KTV Diagnostic Imaging
Harbin Legal Group
Truffords
Banner Template:
4040mm W x 2190mm H Single Sided (.AI)
https://files.example-share.net/d/8ZkQm3TnWp47LcVbXr2YhJd5Fs61Ae/view
QRLMT Logo:
Can be obtained from our website www.qrlmt.org.au

```html
<!DOCTYPE html>
<html lang="en">
<head>
<meta charset="utf-8">
<title>QRLMT Velvet Orchid Gala – Sponsor Backdrop</title>
<link rel="stylesheet" href="https://fonts.googleapis.com/css2?family=Libre+Baskerville:wght@700&family=Questrial&display=swap">
<style>
  :root {
    --page: #ffffff;
    --pink-core: #e2077f;
    --pink-mid: #a11d62;
    --plum: #5a1a3c;
    --edge: #2e1f22;
    --silver-hi: #ffffff;
    --silver-lo: #bdbdbd;
    --ring: rgba(255, 255, 255, 0.35);
    --disc: #ffffff;
    --navy: #1d3a7a;
    --red: #e0203f;
    --purple: #7b4fa0;
    --gold: #c9a227;
    --logo-yellow: #ece423;
    --logo-teal: #11857c;
  }
  * { box-sizing: border-box; margin: 0; padding: 0; }
  html, body {
    width: 1200px; height: 817px; overflow: hidden; background: var(--page);
  }
  .backdrop {
    position: absolute; left: 37px; top: 103px; width: 1128px; height: 612px;
    background: radial-gradient(ellipse 62% 70% at 50% 52%, var(--pink-core) 0%, var(--pink-mid) 32%, var(--plum) 68%, var(--edge) 100%);
    box-shadow: 0 2px 6px rgba(0, 0, 0, 0.45);
    overflow: hidden;
  }
  .emblem {
    position: absolute; left: 498px; top: 32px; width: 132px; height: 137px;
    border-radius: 40% 45% 35% 40%;
    background: linear-gradient(100deg, var(--silver-hi) 0%, var(--logo-yellow) 45%, var(--silver-hi) 70%, var(--logo-teal) 100%);
  }
  .event-title, .website, .thanks {
    position: absolute; left: 0; width: 100%; text-align: center;
    background: linear-gradient(180deg, var(--silver-hi) 30%, var(--silver-lo) 100%);
    -webkit-background-clip: text; background-clip: text; color: transparent;
    filter: drop-shadow(1px 2px 1px rgba(0, 0, 0, 0.35));
  }
  .event-title {
    top: 178px; font: 700 60px/1 "Libre Baskerville", serif; letter-spacing: 0.5px;
  }
  .website {
    top: 250px; font: 400 46px/1 "Questrial", sans-serif;
  }
  .divider {
    position: absolute; left: 425px; top: 314px; width: 274px; height: 2px;
    background: linear-gradient(90deg, transparent, rgba(255,255,255,0.85) 30%, rgba(255,255,255,0.85) 70%, transparent);
  }
  .thanks {
    top: 350px; font: 700 30px/1.1 "Libre Baskerville", serif;
  }
  .sponsor {
    position: absolute; top: 405px; width: 150px; height: 150px; margin-left: -75px;
    border-radius: 50%; background: var(--ring);
    display: flex; align-items: center; justify-content: center;
  }
  .sponsor-disc {
    width: 138px; height: 138px; border-radius: 50%; background: var(--disc);
    display: flex; align-items: center; justify-content: center; gap: 5px;
    padding: 0 14px; text-align: center;
    font: 400 14px/1.15 "Questrial", sans-serif;
  }
  .mark { width: 10px; height: 10px; flex: none; }
  .truffords { left: 235px; } .truffords .sponsor-disc { color: var(--navy); font-size: 18px; }
  .brockden { left: 405px; } .brockden .sponsor-disc { color: var(--red); }
  .ktv { left: 570px; } .ktv .sponsor-disc { color: var(--purple); }
  .eastglen { left: 731px; } .eastglen .sponsor-disc { color: var(--navy); }
  .harbin { left: 894px; } .harbin .sponsor-disc { color: var(--gold); }
</style>
</head>
<body>
  <main class="backdrop">
    <div class="emblem" role="img" aria-label="QRLMT association emblem"></div>
    <h1 class="event-title">QRLMT Velvet Orchid Gala</h1>
    <p class="website">www.qrlmt.org.au</p>
    <div class="divider"></div>
    <h2 class="thanks">Thank you to our sponsors</h2>

    <div class="sponsor truffords"><div class="sponsor-disc">Truffords</div></div>
    <div class="sponsor brockden"><div class="sponsor-disc"><span class="mark" style="background:var(--red)"></span>Brockden Pathology</div></div>
    <div class="sponsor ktv"><div class="sponsor-disc"><span class="mark" style="background:var(--purple);border-radius:50%"></span>KTV Diagnostic Imaging</div></div>
    <div class="sponsor eastglen"><div class="sponsor-disc">EastGlen Radiology</div></div>
    <div class="sponsor harbin"><div class="sponsor-disc">Harbin Legal Group</div></div>
  </main>
</body>
</html>
```